Marrowgate Auctions Business Cards Design Needed

I need a business card design that is modern looking - double sided (maybe just my logo on the back, but open to suggestions) - the overall design is up to you. I want it to be easy to read - not over the top flashy. I already have a company logo which I uploaded so that needs to be used. The colors of my logo are the colors I want on the card... so blue and gray (do need to match the logo colors).

Requirements
Must have
• Would like the card to be sleek, modern and easy to ready

```html
<!DOCTYPE html>
<html lang="en">
<head>
<meta charset="utf-8">
<title>Marrowgate Auctions – Business Cards</title>
<link rel="stylesheet" href="https://fonts.googleapis.com/css2?family=Lato:wght@400;700&display=swap">
<style>
  :root {
    --stage: #3b3d40;
    --card: #2e2e2f;
    --map-light: #4a4948;
    --map-dark: #3a3a3a;
    --blue: #2e7bc4;
    --white: #f4f4f4;
    --muted: #d9d9d9;
  }
  * { box-sizing: border-box; margin: 0; padding: 0; }
  html, body { width: 1200px; height: 900px; overflow: hidden; }
  body {
    background: var(--stage);
    font-family: "Lato", sans-serif;
    color: var(--white);
    position: relative;
  }
  .card {
    position: absolute;
    width: 640px;
    height: 366px;
    left: 280px;
    background: var(--card);
    overflow: hidden;
    box-shadow: 0 10px 30px rgba(0,0,0,.35);
  }
  .card--front { top: 64px; }
  .card--back { top: 470px; }
  .world-map {
    position: absolute;
    inset: 24px 20px 20px 20px;
    background: radial-gradient(ellipse at 50% 45%, var(--map-light) 0%, var(--map-dark) 60%, var(--card) 100%);
    opacity: .7;
    border-radius: 40% 45% 35% 40%;
  }
  .brand {
    position: absolute;
    display: flex;
    align-items: center;
    gap: 12px;
  }
  .brand__mark {
    width: 26px;
    height: 26px;
    background: var(--blue);
    flex: none;
  }
  .brand__name {
    font-weight: 700;
    font-size: 34px;
    letter-spacing: .5px;
    color: var(--white);
    text-transform: uppercase;
    white-space: nowrap;
  }
  .card--front .brand { left: 0; right: 0; top: 138px; justify-content: center; }
  .tagline {
    position: absolute;
    left: 0; right: 0; top: 196px;
    text-align: center;
    font-weight: 700;
    font-size: 19px;
    color: var(--white);
  }
  .card--back .brand { left: 40px; top: 150px; width: 260px; }
  .card--back .brand__name {
    font-size: 26px;
    line-height: 1.1;
    white-space: normal;
  }
  .divider {
    position: absolute;
    left: 330px; top: 96px;
    width: 2px; height: 176px;
    background: var(--blue);
  }
  .contact {
    position: absolute;
    left: 352px; top: 92px;
    line-height: 1.3;
  }
  .contact__name { font-weight: 700; font-size: 22px; color: var(--white); }
  .contact__role { font-size: 14px; color: var(--blue); margin-bottom: 2px; }
  .contact__place { font-size: 15px; color: var(--muted); margin-bottom: 6px; }
  .contact__list { list-style: none; }
  .contact__item {
    display: flex; align-items: center; gap: 12px;
    font-size: 15px; color: var(--muted);
    margin-bottom: 6px;
  }
  .contact__icon { width: 16px; height: 16px; fill: var(--blue); flex: none; }
</style>
</head>
<body>
  <section class="card card--front">
    <div class="world-map" role="img" aria-label="Faint world map in grey tones"></div>
    <div class="brand">
      <span class="brand__mark"></span>
      <span class="brand__name">Marrowgate Auctions</span>
    </div>
    <p class="tagline">Improving Charity Auctions Nationwide</p>
  </section>

  <section class="card card--back">
    <div class="world-map" role="img" aria-label="Faint world map in grey tones"></div>
    <div class="brand">
      <span class="brand__mark"></span>
      <span class="brand__name">Marrowgate<br>Auctions</span>
    </div>
    <div class="divider"></div>
    <div class="contact">
      <p class="contact__name">Rowan Ellery</p>
      <p class="contact__role">Owner | President - Auctioneer</p>
      <p class="contact__place">Cedar Hollow, Oregon, USA</p>
      <ul class="contact__list">
        <li class="contact__item">
          <svg class="contact__icon" viewBox="0 0 24 24"><path d="M6.6 10.8a15.1 15.1 0 0 0 6.6 6.6l2.2-2.2a1 1 0 0 1 1-.25 11.4 11.4 0 0 0 3.6.57 1 1 0 0 1 1 1V20a1 1 0 0 1-1 1A17 17 0 0 1 3 4a1 1 0 0 1 1-1h3.5a1 1 0 0 1 1 1c0 1.250.2 2.450.57 3.57a1 1 0 0 1-.25 1z"/></svg>
          555-014-2277
        </li>
        <li class="contact__item">
          <svg class="contact__icon" viewBox="0 0 24 24"><path d="M2 5h20v14H2z M4 7v.4l8 5.3 8-5.3V7z" fill-rule="evenodd"/></svg>
          bids@marrowgatemail.com
        </li>
        <li class="contact__item">
          <svg class="contact__icon" viewBox="0 0 24 24"><circle cx="12" cy="12" r="10"/><path d="M2 12h20M12 2c3 3 3 17 0 20M12 2c-3 3-3 17 0 20" stroke="#2e2e2f" stroke-width="1.5" fill="none"/></svg>
          www.gavelrally.com
        </li>
      </ul>
    </div>
  </section>
</body>
</html>
```